Meridian Rest Supply Needs Business Card

Looking for a very nice looking business card. Creative but not extravagant. We sell beds and pillows across the U.S. and need something professional but catchy. I have attached the logo.

Name : Dale Fenwick
Title : President
Phone : (800) 417-2964
Email: sleep@quorvana.com
Website: www.quorvana.com

Can be single-sided or double-sided
horizontal or vertical

Can use Blues/Greys

Target Market(s)

Mass Market

Industry/Entity Type

Retail

Contact Information for Business Card

Name : Dale Fenwick
Title : President
Phone : (800) 417-2964
Email: sleep@quorvana.com
Website: www.quorvana.com

Requirements
Must have
• Clean, Modern, Smooth
• Can use Blues/Greys
• On the other side without the information - have something simple like www.quorvana.com or our logo
Nice to have
• Surprise me
Should not have
• Nothing crazy, nothing cluttered

```html
<!DOCTYPE html>
<html lang="en">
<head>
<meta charset="utf-8">
<title>Meridian Rest Supply Business Card</title>
<link rel="stylesheet" href="https://fonts.googleapis.com/css2?family=Open+Sans:wght@300;400;700&display=swap">
<style>
  :root {
    --page: #e9e9ea;
    --card-dark: #27282a;
    --card-light: #c9cacc;
    --brand-blue: #2fa6dc;
    --band-blue: #2a86b8;
    --icon-grey: #b9babc;
    --text-light: #f2f2f2;
  }
  * { margin: 0; padding: 0; box-sizing: border-box; }
  html, body { width: 1200px; height: 844px; overflow: hidden; }
  body {
    background: var(--page);
    font-family: "Open Sans", sans-serif;
    display: flex;
    align-items: center;
    justify-content: center;
    gap: 40px;
  }
  .card {
    position: relative;
    width: 520px;
    height: 297px;
    border-radius: 4px;
    overflow: hidden;
    box-shadow: 0 6px 18px rgba(0,0,0,0.25);
  }
  .card-back {
    background: var(--card-dark);
    display: flex;
    align-items: center;
    justify-content: center;
  }
  .wordmark {
    font-family: "Open Sans", sans-serif;
    font-weight: 300;
    color: var(--brand-blue);
    letter-spacing: 1px;
  }
  .card-back .wordmark { font-size: 78px; }
  .card-front { background: var(--card-dark); }
  .card-front svg.shapes { position: absolute; inset: 0; }
  .card-front .wordmark {
    position: absolute;
    top: 22px;
    left: 0;
    width: 100%;
    text-align: center;
    font-size: 50px;
  }
  .name-ribbon {
    position: absolute;
    top: 128px;
    left: 175px;
    width: 170px;
    height: 46px;
    background: var(--brand-blue);
    color: var(--text-light);
    text-align: center;
    padding-top: 5px;
  }
  .person-name { font-size: 17px; font-weight: 700; line-height: 1.1; }
  .person-title { font-size: 11px; font-weight: 400; }
  .contact {
    position: absolute;
    display: flex;
    flex-direction: column;
    align-items: center;
    gap: 5px;
    color: var(--text-light);
    font-size: 12px;
  }
  .contact-icon {
    width: 26px; height: 26px;
    border-radius: 4px;
    background: var(--icon-grey);
    display: flex; align-items: center; justify-content: center;
  }
  .contact-phone { left: 40px; top: 222px; }
  .contact-email { left: 190px; top: 200px; }
  .contact-web { right: 30px; top: 178px; }
</style>
</head>
<body>
  <section class="card card-back">
    <span class="wordmark">quorvana</span>
  </section>

  <section class="card card-front">
    <svg class="shapes" viewBox="0 0 520 297" width="520" height="297" aria-hidden="true">
      <polygon points="0,0 520,0 520,82 340,126 180,126 0,188" fill="var(--card-light)"/>
      <polygon points="0,188 180,126 340,126 520,82 520,94 340,150 180,150 0,200" fill="var(--band-blue)"/>
    </svg>
    <div class="wordmark">quorvana</div>
    <div class="name-ribbon">
      <div class="person-name">Dale Fenwick</div>
      <div class="person-title">President</div>
    </div>
    <div class="contact contact-phone">
      <span class="contact-icon">
        <svg width="16" height="16" viewBox="0 0 24 24" aria-hidden="true"><path fill="#fff" d="M6.6 10.8a15 15 0 0 0 6.6 6.6l2.2-2.2a1 1 0 0 1 1-.25 11.4 11.4 0 0 0 3.6.57 1 1 0 0 1 1 1V20a1 1 0 0 1-1 1A17 17 0 0 1 3 4a1 1 0 0 1 1-1h3.5a1 1 0 0 1 1 1c0 1.25.2 2.45.57 3.57a1 1 0 0 1-.25 1z"/></svg>
      </span>
      <span>(800) 417-2964</span>
    </div>
    <div class="contact contact-email">
      <span class="contact-icon">
        <svg width="16" height="16" viewBox="0 0 24 24" aria-hidden="true"><rect x="3" y="6" width="18" height="12" fill="#fff"/><path d="M3 6l9 7 9-7" fill="none" stroke="var(--icon-grey)" stroke-width="1.5"/></svg>
      </span>
      <span>sleep@quorvana.com</span>
    </div>
    <div class="contact contact-web">
      <span class="contact-icon">
        <svg width="16" height="16" viewBox="0 0 24 24" aria-hidden="true"><g fill="none" stroke="#fff" stroke-width="1.6"><circle cx="12" cy="12" r="9"/><ellipse cx="12" cy="12" rx="4" ry="9"/><path d="M3 12h18M5 7h14M5 17h14"/></g></svg>
      </span>
      <span>www.quorvana.com</span>
    </div>
  </section>
</body>
</html>
```